依頼概要
■依頼の目的/概要
弊社の社員が着用する名札のデザインをお願いします。

■依頼詳細
社員全員が着用する名札を制作しようと考えております。
名札の素材はアクリルで検討していますが、デザインによって2層タイプのものにしたり、着色したりすることも検討しています。
名札はピン2本で固定しようと考えております。
名札を着用する服は、白のワイシャツ、白のブラウス及び緑色の作業ジャンパーです。

■デザインに必須の情報
名札に載せてほしい情報は、会社のロゴ、会社名及び個人の氏名です。
会社のロゴ及び社名は添付のファイルを参考にしてください。

■デザインに関する要望
シャープでかっちりした感じ、先進的な感じにしていただきたいです。

■弊社のご紹介
弊社は創業108年の住宅用資材を工務店や建設会社に販売する会社です。資材の販売を中心として、建築業界の生産性を向上させるためのシステム開発、各種教育システムの開発、地域の建築業界活性化に資する書籍の出版なども行っております。
社員数は100名、年商30億円の会社です。

その他何かご不明な点がございましたら、お気軽にご質問下さい。
よろしくお願いいたします。

シンプルながらしっかり我が社のイメージも出してくれるからです。しかも作業服に取り付ける場合のワッペンとしても作りやすいデザインでした。

短期間にもかかわらずたくさんのご提案ありがとうございました。
またいろいろとよろしくお願いします。

```html
<!DOCTYPE html>
<html lang="ja">
<head>
<meta charset="utf-8">
<title>名札デザイン</title>
<link rel="stylesheet" href="https://fonts.googleapis.com/css2?family=Noto+Sans+JP:wght@700&family=Noto+Serif+JP:wght@600&display=swap">
<style>
  :root {
    --bg-light: #ffffff;
    --bg-green: #3b7d35;
    --brand-green: #2f8a3a;
    --brand-dot: #2f8a3a;
    --ink: #111111;
    --ink-light: #ffffff;
    --plate-white: #ffffff;
    --plate-black: #050505;
    --outline: #9a9a9a;
  }
  * { margin: 0; padding: 0; box-sizing: border-box; }
  html, body { width: 849px; height: 1200px; overflow: hidden; }
  body {
    position: relative;
    background: linear-gradient(to right, var(--bg-light) 0 424px, var(--bg-green) 424px 100%);
    font-family: "Noto Serif JP", serif;
  }
  .nameplate {
    position: absolute;
    left: 92px;
    width: 665px;
    height: 270px;
  }
  .nameplate svg { position: absolute; inset: 0; width: 665px; height: 270px; }
  .plate-1 { top: 23px; }
  .plate-2 { top: 315px; }
  .plate-3 { top: 607px; }
  .plate-4 { top: 899px; }

  .company {
    position: absolute;
    top: 86px;
    left: 0;
    width: 100%;
    display: flex;
    justify-content: center;
    align-items: center;
    gap: 10px;
    font-family: "Noto Sans JP", sans-serif;
    font-weight: 700;
    font-size: 26px;
    line-height: 1;
    color: var(--brand-green);
    letter-spacing: 2px;
  }
  .company-dot {
    width: 24px;
    height: 24px;
    border-radius: 50%;
    background: var(--brand-dot);
  }
  .person-name {
    position: absolute;
    top: 168px;
    left: 0;
    width: 100%;
    text-align: center;
    font-family: "Noto Serif JP", serif;
    font-weight: 600;
    font-size: 62px;
    line-height: 80px;
    color: var(--ink);
    letter-spacing: 8px;
    white-space: pre;
  }
  .plate-2 .person-name { color: var(--ink-light); }
</style>
</head>
<body>

<div class="nameplate plate-1">
  <svg viewBox="0 0 665 270">
    <polygon points="1,76 332.5,1 664,76 664,269 1,269" fill="var(--plate-white)" stroke="var(--outline)" stroke-width="2"/>
    <line x1="1" y1="156" x2="664" y2="156" stroke="#222" stroke-width="2"/>
  </svg>
  <div class="company"><span class="company-dot"></span><span>株式会社 緑峰</span></div>
  <div class="person-name">山田　太郎</div>
</div>

<div class="nameplate plate-2">
  <svg viewBox="0 0 665 270">
    <polygon points="0,76 332.5,0 665,76 665,270 0,270" fill="var(--plate-black)"/>
    <line x1="0" y1="156" x2="665" y2="156" stroke="#cfcfcf" stroke-width="2"/>
  </svg>
  <div class="company"><span class="company-dot"></span><span>株式会社 緑峰</span></div>
  <div class="person-name">山田　太郎</div>
</div>

<div class="nameplate plate-3">
  <svg viewBox="0 0 665 270">
    <defs>
      <linearGradient id="silver" x1="0" y1="0" x2="1" y2="1">
        <stop offset="0" stop-color="#a9a9a9"/>
        <stop offset="0.3" stop-color="#f2f2f2"/>
        <stop offset="0.55" stop-color="#9c9c9c"/>
        <stop offset="0.8" stop-color="#e4e4e4"/>
        <stop offset="1" stop-color="#8e8e8e"/>
      </linearGradient>
    </defs>
    <polygon points="0,76 332.5,0 665,76 665,270 0,270" fill="url(#silver)"/>
    <line x1="0" y1="156" x2="665" y2="156" stroke="#222" stroke-width="2"/>
  </svg>
  <div class="company"><span class="company-dot"></span><span>株式会社 緑峰</span></div>
  <div class="person-name">山田　太郎</div>
</div>

<div class="nameplate plate-4">
  <svg viewBox="0 0 665 270">
    <defs>
      <linearGradient id="gold" x1="0" y1="0" x2="1" y2="1">
        <stop offset="0" stop-color="#a8956a"/>
        <stop offset="0.3" stop-color="#ece2c4"/>
        <stop offset="0.55" stop-color="#a38f5f"/>
        <stop offset="0.8" stop-color="#ddd0a8"/>
        <stop offset="1" stop-color="#917d50"/>
      </linearGradient>
    </defs>
    <polygon points="0,76 332.5,0 665,76 665,270 0,270" fill="url(#gold)"/>
    <line x1="0" y1="156" x2="665" y2="156" stroke="#222" stroke-width="2"/>
  </svg>
  <div class="company"><span class="company-dot"></span><span>株式会社 緑峰</span></div>
  <div class="person-name">山田　太郎</div>
</div>

</body>
</html>
```